Business Card Design for Cybersecurity Company - Quorvent Systems

We need a business card design for our new cybersecurity company, Quorvent. We’re going for a clean, hi tech look that feels modern, premium, and trustworthy. We want a design that really stands out and makes people say WOW when we hand it over!

Quorvent delivers reliable IT support and managed services for small and mid sized businesses. We help companies stay secure, efficient, and connected through proactive monitoring, cybersecurity services, cloud management, and remote support.

Target Market(s)

Designers should target small and mid sized businesses that need dependable cybersecurity and IT support.

Industry/Entity Type

Cybersecurity, Managed Service Provider, IT services

Contact Information for Business Card

Contact information

Requirements
Must have
• The card should look clean, modern, and tech focused, with the Quorvent logo, clear contact info, and strong readability. It needs to feel premium and professional while still keeping a simple layout that fits a cybersecurity and IT brand.
Nice to have
• Nice to have elements include subtle touches that give the card a modern, tech feel, along with a layout that works well in different background styles.
Should not have
• The card should avoid clutter, loud graphics, or anything that takes attention away from the logo and contact details.

```html
<!DOCTYPE html>
<html lang="en">
<head>
<meta charset="utf-8">
<title>Quorvent Systems – Business Card</title>
<link rel="stylesheet" href="https://fonts.googleapis.com/css2?family=Montserrat:wght@700&family=Quicksand:wght@400;600&display=swap">
<style>
  :root {
    --page-bg: #e4e1e3;
    --card-black: #000000;
    --card-white: #ffffff;
    --band-violet: #33206f;
    --accent-ink: #4650a8;
    --icon-ink: #5a5fbf;
    --body-ink: #2a2a3a;
    --logo-ink: #ffffff;
  }
  * { margin: 0; padding: 0; box-sizing: border-box; }
  html, body { width: 1200px; height: 900px; overflow: hidden; }
  body { background: var(--page-bg); position: relative; font-family: "Quicksand", sans-serif; }

  .card {
    position: absolute;
    left: 260px;
    width: 680px;
    height: 390px;
    border-radius: 20px;
    overflow: hidden;
    background: var(--card-black);
  }
  .card--front { top: 40px; }
  .card--back { top: 470px; }

  .card__art { position: absolute; inset: 0; width: 100%; height: 100%; }

  .wordmark {
    position: absolute;
    display: flex;
    flex-direction: column;
    align-items: flex-end;
    color: var(--logo-ink);
    font-family: "Quicksand", sans-serif;
    font-weight: 600;
    line-height: 1;
  }
  .wordmark__name { letter-spacing: 1px; }
  .wordmark__tag { letter-spacing: 0.55em; margin-right: -0.55em; }

  .card--front .wordmark { right: 36px; top: 150px; }
  .card--front .wordmark__name { font-size: 64px; }
  .card--front .wordmark__tag { font-size: 26px; margin-top: 12px; }

  .card--back .wordmark { left: 26px; top: 212px; }
  .card--back .wordmark__name { font-size: 44px; }
  .card--back .wordmark__tag { font-size: 17px; margin-top: 8px; }

  .contact-block {
    position: absolute;
    right: 22px;
    top: 88px;
    text-align: right;
  }
  .contact-block__name {
    font-family: "Montserrat", sans-serif;
    font-weight: 700;
    font-size: 28px;
    color: var(--accent-ink);
    margin-right: 24px;
    letter-spacing: 0.2px;
  }
  .contact-block__role {
    font-size: 13px;
    color: var(--body-ink);
    margin-right: 24px;
    margin-top: 2px;
  }
  .contact-list { list-style: none; margin-top: 30px; }
  .contact-list__item {
    display: flex;
    justify-content: flex-end;
    align-items: center;
    gap: 8px;
    font-size: 19px;
    color: var(--body-ink);
    height: 34.5px;
  }
  .contact-list__icon { width: 16px; height: 16px; fill: var(--icon-ink); flex: none; }
  .contact-list__icon--line { fill: none; stroke: var(--icon-ink); stroke-width: 1.4; }
</style>
</head>
<body>

<section class="card card--front" aria-label="Card front">
  <svg class="card__art" viewBox="0 0 850 487" preserveAspectRatio="none" aria-hidden="true">
    <path d="M0,300 Q425,300 850,410 L850,462 Q425,355 0,352 Z" fill="var(--band-violet)"/>
  </svg>
  <div class="wordmark">
    <span class="wordmark__name">Quorvent</span>
    <span class="wordmark__tag">Systems</span>
  </div>
</section>

<section class="card card--back" aria-label="Card back">
  <svg class="card__art" viewBox="0 0 850 487" preserveAspectRatio="none" aria-hidden="true">
    <path d="M290,0 L330,0 Q430,260 600,487 L555,487 Q395,270 290,0 Z" fill="var(--band-violet)"/>
    <path d="M330,0 L850,0 L850,487 L600,487 Q430,260 330,0 Z" fill="var(--card-white)"/>
  </svg>

  <div class="wordmark">
    <span class="wordmark__name">Quorvent</span>
    <span class="wordmark__tag">Systems</span>
  </div>

  <div class="contact-block">
    <h1 class="contact-block__name">DANA MERRICK</h1>
    <p class="contact-block__role">OWNER | CEO</p>
    <ul class="contact-list">
      <li class="contact-list__item">P: (855) 310-QRVT
        <svg class="contact-list__icon" viewBox="0 0 16 16" aria-hidden="true"><path d="M4 1.5l2.3 2.8-1.4 1.6c.8 1.9 2.3 3.4 4.2 4.2l1.6-1.4 2.8 2.3-1.6 2.4C6.8 13.2 2.8 9.2 1.6 4.6z"/></svg>
      </li>
      <li class="contact-list__item">M: (555) 014-2286
        <svg class="contact-list__icon" viewBox="0 0 16 16" aria-hidden="true"><path d="M4 1.5l2.3 2.8-1.4 1.6c.8 1.9 2.3 3.4 4.2 4.2l1.6-1.4 2.8 2.3-1.6 2.4C6.8 13.2 2.8 9.2 1.6 4.6z"/></svg>
      </li>
      <li class="contact-list__item">dana@quorvent.com
        <svg class="contact-list__icon" viewBox="0 0 16 16" aria-hidden="true"><path d="M1 3h14v10H1z M2.5 4.5v.4L8 9l5.5-4.1v-.4z" fill-rule="evenodd"/></svg>
      </li>
      <li class="contact-list__item">quorvent.com
        <svg class="contact-list__icon contact-list__icon--line" viewBox="0 0 16 16" aria-hidden="true"><circle cx="8" cy="8" r="6.3"/><ellipse cx="8" cy="8" rx="2.8" ry="6.3"/><path d="M1.7 8h12.6M2.8 4.8h10.4M2.8 11.2h10.4"/></svg>
      </li>
    </ul>
  </div>
</section>

</body>
</html>
```